Business Card Design Project

I need a business card designed from scratch. I have an existing logo that I can upload in Illustrator for modification or redesign.

The Company is called Ranking Oracles http://rankingoracles.com.au and we provide Search Engine Optimization services to Australian businesses. The current logo signifies an increase in visitors, profits etc...

There are no restrictions as to the redesign - colours, style etc are all open to change.

Cards will be full colour and one sided printed at http://www.cardmillo.com.au so check their requirements for file format and sizes etc.

I will expect all original files upon completion of project.

Target Market(s)

Any business with a web site looking to improve their search engine rankings

Industry/Entity Type

Business

Requirements
Must have
• I like modern, sleek designs. Clean, not fussy, uncluttered.

```html
<!DOCTYPE html>
<html lang="en">
<head>
<meta charset="utf-8">
<title>Ranking Oracles – Business Card</title>
<link rel="stylesheet" href="https://fonts.googleapis.com/css2?family=Outfit:wght@300;400;600&display=swap">
<style>
  :root {
    --backdrop: #d9d6d0;
    --card: #ebebe9;
    --brand-blue: #1d6bb0;
    --text-dark: #2a2a2c;
    --rule: #ffffff;
    --icon-blue: #2d6fae;
  }
  * { box-sizing: border-box; margin: 0; padding: 0; }
  html, body {
    width: 1200px;
    height: 900px;
    overflow: hidden;
    background: var(--backdrop);
  }
  body {
    display: flex;
    align-items: center;
    justify-content: center;
    font-family: "Outfit", sans-serif;
  }
  .business-card {
    position: relative;
    width: 840px;
    height: 480px;
    background: var(--card);
    box-shadow: 0 10px 30px rgba(0,0,0,0.15);
  }
  .brand {
    position: absolute;
    top: 70px;
    right: 60px;
    display: flex;
    align-items: center;
    gap: 14px;
  }
  .brand-dot {
    width: 30px;
    height: 30px;
    border-radius: 50%;
    background: var(--brand-blue);
  }
  .brand-name {
    font-size: 42px;
    font-weight: 600;
    color: var(--brand-blue);
    letter-spacing: 0.2px;
  }
  .identity {
    position: absolute;
    left: 52px;
    top: 150px;
    color: var(--brand-blue);
  }
  .identity-name {
    font-size: 30px;
    font-weight: 600;
  }
  .identity-role {
    font-size: 28px;
    font-weight: 300;
    margin-top: 2px;
  }
  .divider {
    position: absolute;
    left: 0;
    top: 250px;
    width: 350px;
    height: 2px;
    background: var(--rule);
  }
  .contact-list {
    position: absolute;
    left: 52px;
    top: 285px;
    list-style: none;
    color: var(--text-dark);
    font-size: 23px;
    font-weight: 300;
  }
  .contact-item {
    display: flex;
    align-items: center;
    gap: 14px;
    height: 42px;
  }
  .contact-icon {
    width: 18px;
    height: 18px;
    fill: var(--icon-blue);
    flex-shrink: 0;
  }
</style>
</head>
<body>
  <article class="business-card">
    <div class="brand">
      <span class="brand-dot"></span>
      <span class="brand-name">Ranking Oracles</span>
    </div>

    <div class="identity">
      <p class="identity-name">Daniel Hart</p>
      <p class="identity-role">Director</p>
    </div>

    <div class="divider"></div>

    <ul class="contact-list">
      <li class="contact-item">
        <svg class="contact-icon" viewBox="0 0 24 24" aria-hidden="true"><path d="M6.6 10.8a15.1 15.1 0 0 0 6.6 6.6l2.2-2.2a1 1 0 0 1 1-.25 11.4 11.4 0 0 0 3.6.57 1 1 0 0 1 1 1V20a1 1 0 0 1-1 1A17 17 0 0 1 3 4a1 1 0 0 1 1-1h3.5a1 1 0 0 1 1 1c0 1.25.2 2.45.57 3.57a1 1 0 0 1-.25 1z"/></svg>
        <span>1300 482915</span>
      </li>
      <li class="contact-item">
        <svg class="contact-icon" viewBox="0 0 24 24" aria-hidden="true"><path d="M8 2h8a2 2 0 0 1 2 2v16a2 2 0 0 1-2 2H8a2 2 0 0 1-2-2V4a2 2 0 0 1 2-2zm0 3v11h8V5zm4 13a1 1 0 1 0 0 2 1 1 0 0 0 0-2z"/></svg>
        <span>+ 61 (0)2 9471 3025</span>
      </li>
      <li class="contact-item">
        <svg class="contact-icon" viewBox="0 0 24 24" aria-hidden="true"><path d="M2 5h20v14H2zm2 2v.5l8 5 8-5V7zm0 2.8V17h16V9.8l-8 5z"/></svg>
        <span>enquiry@rankingoracles.com.au</span>
      </li>
      <li class="contact-item">
        <svg class="contact-icon" viewBox="0 0 24 24" aria-hidden="true"><path d="M12 2a10 10 0 1 0 0 20 10 10 0 0 0 0-20zm6.9 9h-3a15 15 0 0 0-1.2-5.4A8 8 0 0 1 18.9 11zM12 4c.9 1.2 1.8 3.6 1.9 7h-3.8c.1-3.4 1-5.8 1.9-7zM9.3 5.6A15 15 0 0 0 8.1 11h-3a8 8 0 0 1 4.2-5.4zM5.1 13h3a15 15 0 0 0 1.2 5.4A8 8 0 0 1 5.1 13zM12 20c-.9-1.2-1.8-3.6-1.9-7h3.8c-.1 3.4-1 5.8-1.9 7zm2.7-1.6a15 15 0 0 0 1.2-5.4h3a8 8 0 0 1-4.2 5.4z"/></svg>
        <span>www.rankingoracles.com.au</span>
      </li>
    </ul>
  </article>
</body>
</html>
```